UPDATED BRIEF: We are looking for a trade show booth design - The design is for 10ft x 10 ft booth curved booth display.
we want to utilize the laptop image more with a half wheel of the key services on our platform.
Strategic DEI Business Partner Workshops
Leader to Leader Training
ERG Leader Strategic Training
15 - Microlearning Labs
Coaching & Mentorship
DEI Research, Articles and Hot topics

With the tagline: Experience the Power of Strategic DEI Training and Peer-to-Peer Support on One Platform

About us: we are a learning and development community for diversity and inclusion and talent management professionals. Our corporate colors are blue, 004AAD
We are looking for a clean, corporate design that makes someone feel included. The moment you look at it, you feel included. We may add a screenshot of the Brightpath Growth Studio platform. Our logo will be included and our tagline is

"Together We Can Create a More Inclusive Future: The Brightpath Growth Studio Community for DEI and Talent Leaders."

We have two versions of our logo - one with text only the other with the logo design. We're not sure which one we want to use.

Target Market(s)

Human Resources and Talent Leaders

Industry/Entity Type

Training and development

Colors
0054AA
0677BA
7BADD7
CADEEF
E8F1F8
F0912C
F2A743
F7CA91
FBE8D2
FDF5EE
EB3D1F
EC4F4E
F09395
F8D3D4
FCEDEE

Requirements
Must have
• Must have logo and good visual design
Should not have
• I've added the examples of what I am looking for

```html
<!DOCTYPE html>
<html lang="en">
<head>
<meta charset="utf-8">
<title>Brightpath Growth Studio – Booth Backdrop</title>
<link rel="stylesheet" href="https://fonts.googleapis.com/css2?family=Montserrat:wght@300;400;600;700;800&display=swap">
<style>
  :root {
    --page-bg: #e6e6e6;
    --brand-blue: #1d47a6;
    --navy: #1b2a55;
    --white: #ffffff;
    --red: #e5452b;
    --orange: #ee7a2e;
    --amber: #f2a743;
    --teal: #2f8bc0;
    --sky: #3ba0da;
    --light-sky: #7bc0ee;
    --ring: #d5d9e2;
    --icon-line: #7a8291;
    --url-orange: #e8521f;
  }
  html, body {
    margin: 0;
    padding: 0;
    width: 857px;
    height: 1200px;
    overflow: hidden;
    background: var(--page-bg);
    font-family: "Montserrat", sans-serif;
  }
  .canvas {
    position: relative;
    width: 857px;
    height: 1200px;
  }
  .booth-backdrop {
    position: absolute;
    left: 28px;
    top: 349px;
    width: 800px;
    height: 502px;
    filter: drop-shadow(0 14px 18px rgba(0,0,0,0.28));
  }
  .brand-name { font-weight: 700; fill: var(--white); }
  .tagline { font-weight: 700; fill: var(--white); }
  .award-line { font-weight: 600; fill: var(--white); }
  .award-title { font-weight: 800; fill: var(--white); }
  .side-url { fill: var(--white); }
  .url-light { font-weight: 300; }
  .url-bold { font-weight: 700; }
  .service-label { font-weight: 600; fill: var(--navy); font-size: 10.5px; }
  .service-number { font-weight: 700; fill: var(--white); font-size: 21px; }
  .footer-url { font-size: 27px; }
  .footer-url .url-www, .footer-url .url-tld { fill: var(--brand-blue); font-weight: 400; }
  .footer-url .url-name { fill: var(--url-orange); font-weight: 700; }
</style>
</head>
<body>
<main class="canvas">
  <svg class="booth-backdrop" viewBox="0 0 1172 735" xmlns="http://www.w3.org/2000/svg">
    <defs>
      <linearGradient id="headerGradient" x1="0" y1="0" x2="1" y2="0">
        <stop offset="0" stop-color="#e3432a"/>
        <stop offset="1" stop-color="#e99a3d"/>
      </linearGradient>
      <linearGradient id="cardGradient" x1="0" y1="0" x2="0" y2="1">
        <stop offset="0" stop-color="#ffffff"/>
        <stop offset="1" stop-color="#e4e8ef"/>
      </linearGradient>
      <linearGradient id="screenGradient" x1="0" y1="0" x2="1" y2="0">
        <stop offset="0" stop-color="#1b2a55"/>
        <stop offset="0.3" stop-color="#1b2a55"/>
        <stop offset="0.3" stop-color="#f4f5f8"/>
        <stop offset="1" stop-color="#ffffff"/>
      </linearGradient>
    </defs>

    <!-- Body -->
    <rect class="backdrop-body" x="0" y="0" width="1172" height="735" fill="var(--brand-blue)"/>

    <!-- Header band -->
    <path class="header-band" d="M0 0 H1172 V85 Q586 250 0 90 Z" fill="url(#headerGradient)"/>
    <text class="brand-name" x="586" y="110" text-anchor="middle" font-size="44">Brightpath Growth Studio</text>

    <!-- Footer wave -->
    <path class="footer-wave" d="M0 705 Q586 545 1172 700 V735 H0 Z" fill="var(--white)"/>
    <text class="footer-url" x="587" y="692" text-anchor="middle"><tspan class="url-www">www.</tspan><tspan class="url-name">brightpathgrowthstudio</tspan><tspan class="url-tld">.com</tspan></text>

    <!-- Side URLs -->
    <text class="side-url" font-size="23" text-anchor="middle" transform="translate(58 400) rotate(-90)"><tspan class="url-light">www.</tspan><tspan class="url-bold">brightpathgrowthstudio</tspan><tspan class="url-light">.com</tspan></text>
    <text class="side-url" font-size="23" text-anchor="middle" transform="translate(1114 370) rotate(90)"><tspan class="url-light">www.</tspan><tspan class="url-bold">brightpathgrowthstudio</tspan><tspan class="url-light">.com</tspan></text>

    <!-- Tagline -->
    <g class="tagline" font-size="20" text-anchor="middle">
      <text x="357" y="215">Experience the Power of Strategic</text>
      <text x="357" y="242">DEI Training and Peer-to-Peer Support</text>
      <text x="357" y="269">on One Platform</text>
    </g>

    <!-- Laptop -->
    <g class="laptop">
      <rect x="190" y="283" width="335" height="234" rx="8" fill="#202124"/>
      <rect x="198" y="290" width="319" height="216" fill="url(#screenGradient)" role="img" aria-label="Screenshot of the Brightpath Growth Studio community platform home page"/>
      <path d="M180 515 H565 L558 525 H188 Z" fill="#b9bcc2"/>
    </g>

    <!-- Award -->
    <text class="award-line" x="352" y="557" text-anchor="middle" font-size="15">Award Wining Innovative Platform for DEL Leaders</text>
    <text class="award-title" x="352" y="581" text-anchor="middle" font-size="17">WINNER 2021 DIVERSITY INNOVATORS AWARD</text>

    <!-- Half wheel -->
    <g class="service-wheel" fill="none" stroke="var(--white)" stroke-width="2">
      <path d="M585 262 Q745 400 585 536"/>
      <polyline points="585,262 612,222 718,222"/>
      <line x1="640" y1="303" x2="733" y2="293"/>
      <line x1="668" y1="365" x2="755" y2="363"/>
      <line x1="668" y1="432" x2="755" y2="433"/>
      <line x1="638" y1="493" x2="733" y2="503"/>
      <polyline points="585,536 612,573 690,573"/>
    </g>
    <g class="wheel-nodes" stroke="var(--white)" stroke-width="3">
      <circle cx="585" cy="262" r="7" fill="var(--red)"/>
      <circle cx="640" cy="303" r="7" fill="var(--orange)"/>
      <circle cx="668" cy="365" r="7" fill="var(--amber)"/>
      <circle cx="668" cy="432" r="7" fill="var(--teal)"/>
      <circle cx="638" cy="493" r="7" fill="var(--sky)"/>
      <circle cx="585" cy="536" r="7" fill="var(--light-sky)"/>
      <circle cx="718" cy="222" r="5" fill="var(--red)" stroke-width="2"/>
      <circle cx="733" cy="293" r="5" fill="var(--orange)" stroke-width="2"/>
      <circle cx="755" cy="363" r="5" fill="var(--amber)" stroke-width="2"/>
      <circle cx="755" cy="433" r="5" fill="var(--teal)" stroke-width="2"/>
      <circle cx="733" cy="503" r="5" fill="var(--sky)" stroke-width="2"/>
      <circle cx="690" cy="573" r="5" fill="var(--light-sky)" stroke-width="2"/>
    </g>

    <!-- Service pills -->
    <g class="service-item">
      <rect x="735" y="197" width="232" height="50" rx="25" fill="var(--red)"/>
      <rect x="735" y="197" width="192" height="50" rx="25" fill="url(#cardGradient)"/>
      <circle cx="735" cy="222" r="28" fill="var(--white)" stroke="var(--ring)" stroke-width="2"/>
      <circle cx="735" cy="222" r="12" fill="none" stroke="var(--icon-line)" stroke-width="1.5"/>
      <text class="service-label" x="770" y="218">Strategic DEI Business</text>
      <text class="service-label" x="770" y="232">Partner Workshops</text>
      <text class="service-number" x="947" y="230" text-anchor="middle">01</text>
    </g>
    <g class="service-item">
      <rect x="780" y="267" width="232" height="50" rx="25" fill="var(--orange)"/>
      <rect x="780" y="267" width="192" height="50" rx="25" fill="url(#cardGradient)"/>
      <circle cx="780" cy="292" r="28" fill="var(--white)" stroke="var(--ring)" stroke-width="2"/>
      <circle cx="780" cy="292" r="12" fill="none" stroke="var(--icon-line)" stroke-width="1.5"/>
      <text class="service-label" x="818" y="288">Leader to</text>
      <text class="service-label" x="818" y="302">Leader Training</text>
      <text class="service-number" x="992" y="300" text-anchor="middle">02</text>
    </g>
    <g class="service-item">
      <rect x="802" y="338" width="232" height="50" rx="25" fill="var(--amber)"/>
      <rect x="802" y="338" width="192" height="50" rx="25" fill="url(#cardGradient)"/>
      <circle cx="802" cy="363" r="28" fill="var(--white)" stroke="var(--ring)" stroke-width="2"/>
      <circle cx="802" cy="363" r="12" fill="none" stroke="var(--icon-line)" stroke-width="1.5"/>
      <text class="service-label" x="842" y="359">ERG Leader</text>
      <text class="service-label" x="842" y="373">Strategic Training</text>
      <text class="service-number" x="1014" y="371" text-anchor="middle">03</text>
    </g>
    <g class="service-item">
      <rect x="802" y="407" width="232" height="50" rx="25" fill="var(--teal)"/>
      <rect x="802" y="407" width="192" height="50" rx="25" fill="url(#cardGradient)"/>
      <circle cx="802" cy="432" r="28" fill="var(--white)" stroke="var(--ring)" stroke-width="2"/>
      <circle cx="802" cy="432" r="12" fill="none" stroke="var(--icon-line)" stroke-width="1.5"/>
      <text class="service-label" x="836" y="436">15 - Microlearning Labs</text>
      <text class="service-number" x="1014" y="440" text-anchor="middle">04</text>
    </g>
    <g class="service-item">
      <rect x="780" y="475" width="232" height="50" rx="25" fill="var(--sky)"/>
      <rect x="780" y="475" width="192" height="50" rx="25" fill="url(#cardGradient)"/>
      <circle cx="780" cy="500" r="28" fill="var(--white)" stroke="var(--ring)" stroke-width="2"/>
      <circle cx="780" cy="500" r="12" fill="none" stroke="var(--icon-line)" stroke-width="1.5"/>
      <text class="service-label" x="818" y="496">Coaching &amp;</text>
      <text class="service-label" x="818" y="510">Mentorship</text>
      <text class="service-number" x="992" y="508" text-anchor="middle">05</text>
    </g>
    <g class="service-item">
      <rect x="738" y="545" width="232" height="50" rx="25" fill="var(--light-sky)"/>
      <rect x="738" y="545" width="192" height="50" rx="25" fill="url(#cardGradient)"/>
      <circle cx="738" cy="570" r="28" fill="var(--white)" stroke="var(--ring)" stroke-width="2"/>
      <circle cx="738" cy="570" r="12" fill="none" stroke="var(--icon-line)" stroke-width="1.5"/>
      <text class="service-label" x="774" y="566">DEI Research, Articles</text>
      <text class="service-label" x="774" y="580">and Hot topics</text>
      <text class="service-number" x="950" y="578" text-anchor="middle">06</text>
    </g>
  </svg>
</main>
</body>
</html>
```